Eastvale Physiotherapy Website www.eastvalephysiotherapy.com.au

Create Wordpress website for Eastvale Physiotherapy which aligns with our other locations www.marrowbankphysiotherapy,com.au. We would like the website to present in a similar fashion to our exisiting site with similar headings and layout. We will then alter the text to make it location specific.

Coding

Coded - Design and coding required

Number of Pages Required

1 page

Font styles to use
Sans Serif

Requirements
Must have
• Colours of the website must match the colours of the colour Eastvale Physiotherapy logo
• Website must be complimentary to existing websites,
• www.marrowbankphysiotherapy.com.au
• www.marrowbankpilatesandrehab.com.au

```html
<!DOCTYPE html>
<html lang="en">
<head>
<meta charset="utf-8">
<title>Eastvale Physiotherapy</title>
<link rel="stylesheet" href="https://fonts.googleapis.com/css2?family=Montserrat:wght@400;600;700&family=Open+Sans:wght@400;600;700&display=swap">
<style>
:root{
  --navy:#2d2f6b;
  --indigo:#3b3c86;
  --teal:#66c1a4;
  --teal-dark:#4fae8f;
  --purple:#6a4fa3;
  --ink:#2b2b3a;
  --body:#7a7f8c;
  --line:#e3e5ea;
  --foot:#e9ebef;
  --foot-bar:#dadce1;
  --white:#ffffff;
}
*{box-sizing:border-box;margin:0;padding:0}
html,body{width:1200px;height:3005px;overflow:hidden;background:var(--white)}
body{position:relative;font-family:"Open Sans",Arial,sans-serif;color:var(--ink)}
.abs{position:absolute}
.head-font{font-family:"Montserrat",Arial,sans-serif}

/* top bar */
.topbar{left:90px;top:0;width:1020px;height:36px;background:var(--navy);border-radius:0 0 26px 26px;color:#d6d8ee;font-size:13px}
.topbar .item{top:10px;display:flex;align-items:center;gap:8px}
.social{top:9px;right:70px;display:flex;gap:12px}
.social span{width:16px;height:16px;border-radius:50%;background:#c9cbe6;opacity:.8}

/* header */
.logo{display:flex;align-items:center;gap:10px;font-family:"Montserrat",Arial,sans-serif;font-weight:700;color:var(--navy);font-size:20px}
.logo .dot{width:26px;height:26px;border-radius:50%;background:var(--teal)}
.nav{top:84px;left:394px;display:flex;gap:27px;font-family:"Montserrat",Arial,sans-serif;font-weight:600;font-size:13px;color:var(--ink)}

/* hero */
.hero{left:0;top:140px;width:1200px;height:552px;background:linear-gradient(100deg,#d9dbdd 0%,#eceeef 35%,#f3f3f2 55%,#c9b8a6 75%,#7d7a78 100%)}
.hero h1{position:absolute;left:0;width:1164px;top:160px;text-align:center;font-family:"Montserrat",Arial,sans-serif;font-weight:700;font-size:36px;color:var(--navy);letter-spacing:.5px}
.hero h2{position:absolute;left:0;width:1164px;top:216px;text-align:center;font-family:"Montserrat",Arial,sans-serif;font-weight:600;font-size:19px;color:var(--ink);letter-spacing:.5px}
.btn{position:absolute;left:472px;top:268px;width:220px;height:46px;border-radius:23px;background:var(--teal);color:#fff;font-family:"Montserrat",Arial,sans-serif;font-weight:600;font-size:14px;display:flex;align-items:center;justify-content:center}

/* partners */
.partners{left:0;top:692px;width:1200px;height:98px;border-bottom:1px solid var(--line);display:flex;justify-content:space-between;align-items:center;padding:0 128px}
.partners span{font-family:"Montserrat",Arial,sans-serif;font-weight:700;font-size:20px;color:#9a9ca3}
.partners span.dark{color:#1c1c22}

/* intro cards */
.intro-box{left:114px;top:872px;width:306px;height:346px;border:3px solid #e7e8ec;padding:36px 30px}
.intro-box h3{font-family:"Montserrat",Arial,sans-serif;font-weight:600;font-size:18px;color:var(--ink);margin-bottom:16px}
.intro-box p{font-size:12.5px;line-height:23px;color:var(--body)}
.link{font-family:"Montserrat",Arial,sans-serif;font-weight:600;font-size:14px;color:var(--purple)}
.intro-box .link{display:block;margin-top:14px}
.card{width:308px}
.card .ph{height:184px}
.card h4{margin-top:32px;font-family:"Montserrat",Arial,sans-serif;font-weight:700;font-size:15px;color:var(--ink)}
.card p{margin-top:14px;font-size:12.5px;line-height:22px;color:var(--body)}
.card .link{display:block;margin-top:12px;font-size:13px}

/* services */
.services{left:0;top:1322px;width:1200px;height:780px;background:linear-gradient(120deg,#3a3b85 0%,#41438d 45%,#4a4c93 70%,#3c3d86 100%)}
.services .eyebrow{position:absolute;top:50px;width:1164px;text-align:center;font-family:"Montserrat",Arial,sans-serif;font-weight:600;font-size:11px;letter-spacing:1px;color:var(--teal)}
.services h2{position:absolute;top:84px;width:1164px;text-align:center;font-family:"Montserrat",Arial,sans-serif;font-weight:700;font-size:28px;color:#fff}
.spine{position:absolute;left:578px;top:158px;width:12px;height:474px;border-radius:6px;background:#e4e5ee}
.knot{position:absolute;left:578px;width:12px;height:12px;border-radius:50%;background:#fff;border:2px solid #b9bbd2}
.svc{position:absolute;width:230px;color:#fff}
.svc.left{left:196px;text-align:right}
.svc.right{left:726px}
.svc h5{font-family:"Montserrat",Arial,sans-serif;font-weight:700;font-size:14px;margin-bottom:4px}
.svc p{font-size:11.5px;line-height:15px;color:#e7e8f4}
.ic{position:absolute;width:64px;height:64px;border-radius:50%;background:var(--teal);display:flex;align-items:center;justify-content:center}

/* blog */
.blog-title{left:0;top:2180px;width:1164px;text-align:center;font-family:"Montserrat",Arial,sans-serif;font-weight:600;font-size:28px;color:#45464f}
.post{width:292px;height:288px;border:1px solid var(--line);top:2270px}
.post .date{position:absolute;left:0;top:0;width:94px;height:102px;background:#ececee;text-align:center;font-family:"Montserrat",Arial,sans-serif;color:#45464f}
.post .date.on{background:var(--teal);color:#fff}
.post .date b{display:block;font-weight:400;font-size:32px;margin-top:18px;line-height:36px}
.post .date i{font-style:normal;font-weight:600;font-size:15px}
.post .ph{position:absolute;left:94px;top:0;right:0;height:102px}
.post h4{position:absolute;left:12px;top:112px;font-family:"Open Sans",Arial,sans-serif;font-weight:600;font-size:14.5px;color:var(--ink)}
.post h4.on{color:var(--teal-dark)}
.post p{position:absolute;left:12px;right:14px;top:158px;font-size:11px;line-height:17px;color:var(--body)}
.post .more{position:absolute;left:12px;top:224px;font-size:11px;color:var(--teal)}
.post .meta{position:absolute;left:0;right:0;bottom:0;height:32px;border-top:1px solid var(--line);display:flex;align-items:center;gap:8px;padding-left:12px;font-size:10px;color:var(--body)}

/* footer */
.footer{left:0;top:2626px;width:1200px;height:326px;background:var(--foot)}
.footer .about{position:absolute;left:126px;top:152px;width:300px;font-size:13px;line-height:19px;color:var(--body)}
.hours{position:absolute;left:448px;top:74px;width:296px}
.hours h3{font-family:"Montserrat",Arial,sans-serif;font-weight:700;font-size:20px;color:var(--ink);margin-bottom:12px}
.hours .row{display:flex;justify-content:space-between;padding:9px 0 10px;border-bottom:1px solid #c8cad0;font-family:"Montserrat",Arial,sans-serif;font-weight:600;font-size:12px;color:var(--ink)}
.hours .row:last-child{border-bottom:0}
.hours .row span:last-child{width:124px}
.contact-box{position:absolute;left:786px;top:46px;width:300px;height:236px;background:var(--teal);color:#fff;padding:26px 24px}
.contact-box .emg{display:flex;gap:14px;align-items:center;padding-bottom:18px;border-bottom:1px solid rgba(255,255,255,.4)}
.contact-box .emg small{display:block;font-size:12px;opacity:.9}
.contact-box .emg strong{font-family:"Montserrat",Arial,sans-serif;font-size:16px}
.contact-box .line{display:flex;gap:14px;align-items:center;margin-top:18px;font-size:12px;font-weight:600}
.copyright{left:0;top:2952px;width:1200px;height:53px;background:var(--foot-bar);display:flex;align-items:center;justify-content:center;font-size:11.5px;color:#7d8088}
</style>
</head>
<body>

<!-- top bar -->
<div class="abs topbar">
  <div class="abs item" style="left:36px">
    <svg width="12" height="12" viewBox="0 0 24 24"><path d="M6 2l4 5-2 3c1 3 3 5 6 6l3-2 5 4-3 4C10 21 3 14 2 5z" fill="#d6d8ee"/></svg>
    +(1800) 000 4127
  </div>
  <div class="abs item" style="left:180px">
    <svg width="13" height="10" viewBox="0 0 26 20"><rect x="1" y="1" width="24" height="18" fill="none" stroke="#d6d8ee" stroke-width="2"/><path d="M1 1l12 10L25 1" fill="none" stroke="#d6d8ee" stroke-width="2"/></svg>
    info@eastvalephysio.example
  </div>
  <div class="abs social"><span></span><span></span><span></span><span></span><span></span></div>
</div>

<!-- header -->
<div class="abs logo" style="left:86px;top:66px"><span class="dot"></span>Eastvale Physiotherapy</div>
<nav class="abs nav">
  <span>HOME</span><span>ABOUT US</span><span>CLIENT PATHWAYS/ MODEL OF CARE</span><span>SERVICES</span><span>BLOG</span><span>CAREERS</span><span>CONTACT</span>
</nav>

<!-- hero -->
<section class="abs hero" role="img" aria-label="Photo of a therapist examining a patient's ankle on a treatment table">
  <h1>BEST CHIROPRACTORS</h1>
  <h2>AND PHYSICAL THERAPISTS</h2>
  <div class="btn">BOOK APPOINTMENT</div>
</section>

<!-- partners -->
<div class="abs partners">
  <span class="dark">HARLOW</span><span>Linen &amp; Loft</span><span style="font-size:12px;letter-spacing:2px">COPPER TABLE</span><span>wren</span><span>parcelo</span><span style="font-size:16px">No. 9</span>
</div>

<!-- intro -->
<div class="abs intro-box">
  <h3>Eastvale Physiotherapy</h3>
  <p>Here at Eastvale physiotherapy clinic we strive to provide you with an exceptional quality of care across all our services which range from, physiotherapy, ergonomics and more. All therapy services are carried out by experienced and fully trained experts. To see our full range of therapy services please click on the link below.</p>
  <span class="link">All Services</span>
</div>
<div class="abs card" style="left:446px;top:872px">
  <div class="ph" role="img" aria-label="Photo of a therapist treating a client's neck" style="background:linear-gradient(135deg,#f1ebe6,#e2cfc2 60%,#c9b3a4)"></div>
  <h4>Sports Injuries</h4>
  <p>Aenean lacinia bibendum nulla sed consectetur. Aenean eu leo quam. Pellentesque ornare sem lacinia quam venenatis vestibulum....</p>
  <span class="link">Read More</span>
</div>
<div class="abs card" style="left:780px;top:872px">
  <div class="ph" role="img" aria-label="Photo of a seated sports massage session" style="background:linear-gradient(135deg,#eef2f5,#dfe6ea 55%,#b9c9c7)"></div>
  <h4>Sports Massage</h4>
  <p>Aenean lacinia bibendum nulla sed consectetur. Aenean eu leo quam. Pellentesque ornare sem lacinia quam venenatis vestibulum....</p>
  <span class="link">Read More</span>
</div>

<!-- services -->
<section class="abs services" aria-label="Our services">
  <div class="eyebrow">OUR SERVICES</div>
  <h2>What We Do</h2>
  <div class="spine"></div>
  <div class="knot" style="top:186px"></div>
  <div class="knot" style="top:302px"></div>
  <div class="knot" style="top:420px"></div>
  <div class="knot" style="top:538px"></div>

  <div class="svc left" style="top:176px"><h5>Pilates</h5><p>Sed ut perspiciatis unde omnis iste natus error sit voluptatem accusa.</p></div>
  <div class="svc left" style="top:294px"><h5>Physiotherapy</h5><p>Sed ut perspiciatis unde omnis iste natus error sit voluptatem accusa.</p></div>
  <div class="svc left" style="top:412px"><h5>Podiatry</h5><p>Sed ut perspiciatis unde omnis iste natus error sit voluptatem accusa.</p></div>
  <div class="svc left" style="top:530px"><h5>Real Time Ultrasound</h5><p>Sed ut perspiciatis unde omnis iste natus error sit voluptatem accusa.</p></div>

  <div class="svc right" style="top:184px"><h5>Women's &amp; Men's Health</h5><p>Sed ut perspiciatis unde omnis iste natus error sit voluptatem accusa.</p></div>
  <div class="svc right" style="top:302px"><h5>Dignostic Medicine</h5><p>Sed ut perspiciatis unde omnis iste natus error sit voluptatem accusa.</p></div>
  <div class="svc right" style="top:420px"><h5>Other Services</h5><p>Sed ut perspiciatis unde omnis iste natus error sit voluptatem accusa.</p></div>
  <div class="svc right" style="top:538px"><h5>General Surgery</h5><p>Sed ut perspiciatis unde omnis iste natus error sit voluptatem accusa.</p></div>

  <div class="ic" style="left:444px;top:180px"><svg width="30" height="30" viewBox="0 0 30 30" fill="none" stroke="#fff" stroke-width="2.5" stroke-linecap="round"><circle cx="18" cy="6" r="3" fill="#fff"/><path d="M17 11l-4 8h8M13 19l-5 6M21 19l2 6"/></svg></div>
  <div class="ic" style="left:444px;top:298px"><svg width="30" height="30" viewBox="0 0 30 30" fill="none" stroke="#fff" stroke-width="2.5" stroke-linecap="round"><circle cx="17" cy="5" r="3" fill="#fff"/><path d="M16 10l-3 8 5 4-2 6M13 18l-5 6M10 13l6-3 5 4"/></svg></div>
  <div class="ic" style="left:444px;top:416px"><svg width="30" height="30" viewBox="0 0 30 30" fill="none" stroke="#fff" stroke-width="2.5"><circle cx="15" cy="15" r="10"/><path d="M10 15h10M15 10v10"/></svg></div>
  <div class="ic" style="left:444px;top:534px"><svg width="30" height="30" viewBox="0 0 30 30" fill="none" stroke="#fff" stroke-width="2.5"><rect x="4" y="6" width="20" height="14" rx="1"/><path d="M10 25h8M14 20v5"/></svg></div>

  <div class="ic" style="left:644px;top:180px"><svg width="30" height="30" viewBox="0 0 30 30" fill="#fff"><circle cx="9" cy="6" r="3"/><circle cx="21" cy="6" r="3"/><path d="M6 11h6l2 8h-3v8H8v-8H4zM18 11h6v9h-1v7h-4v-7h-1z"/></svg></div>
  <div class="ic" style="left:644px;top:298px"><svg width="30" height="30" viewBox="0 0 30 30" fill="none" stroke="#fff" stroke-width="2.5" stroke-linecap="round"><path d="M7 4v8a5 5 0 0010 0V4M12 17v4a5 5 0 0010 0v-3"/><circle cx="22" cy="15" r="3"/></svg></div>
  <div class="ic" style="left:644px;top:416px"><svg width="30" height="30" viewBox="0 0 30 30" fill="none" stroke="#fff" stroke-width="2.5"><circle cx="15" cy="15" r="10"/><path d="M11 15l3 3 6-6"/></svg></div>
  <div class="ic" style="left:644px;top:534px"><svg width="30" height="30" viewBox="0 0 30 30" fill="#fff"><path d="M15 4c4 6 7 10 7 14a7 7 0 01-14 0c0-4 3-8 7-14z"/></svg></div>
</section>

<!-- blog -->
<h2 class="abs blog-title">Latest Blog</h2>

<article class="abs post" style="left:114px">
  <div class="date"><b>26</b><i>MAY</i></div>
  <div class="ph" role="img" aria-label="Photo of a family walking in a green field under a blue sky" style="background:linear-gradient(180deg,#5a8fd6 0%,#a9c9ef 55%,#6fae3c 56%,#4f8d2a 100%)"></div>
  <h4>Nunc id ligula gravidant</h4>
  <p>Nullas tempus neque massa id mollis neque fesrli convallis ut. Morbi estr velit tincidunt quis felis etv consequat mollis nibhar. Aliquam porttitor</p>
  <span class="more">Read more ›</span>
  <div class="meta"><svg width="9" height="11" viewBox="0 0 18 22"><path d="M9 0a8 8 0 018 8c0 6-8 14-8 14S1 14 1 8a8 8 0 018-8z" fill="#7a7f8c"/></svg>12, Mill Road, Eastvale</div>
</article>

<article class="abs post" style="left:438px">
  <div class="date on"><b>20</b><i>JUN<br>2018</i></div>
  <div class="ph" role="img" aria-label="Photo of smiling children lying in a circle" style="background:linear-gradient(135deg,#f4d34e,#e6a24a 50%,#7fb0d8)"></div>
  <h4 class="on">Suspendisse nec lorem vitae</h4>
  <p>Nullas tempus neque massa id mollis neque fesrli convallis ut. Morbi estr velit tincidunt quis felis etv consequat mollis nibhar. Aliquam porttitor</p>
  <span class="more">Read more ›</span>
  <div class="meta"><svg width="9" height="11" viewBox="0 0 18 22"><path d="M9 0a8 8 0 018 8c0 6-8 14-8 14S1 14 1 8a8 8 0 018-8z" fill="#7a7f8c"/></svg>12, Mill Road, Eastvale</div>
</article>

<article class="abs post" style="left:762px">
  <div class="date"><b>25</b><i>JUL</i></div>
  <div class="ph" role="img" aria-label="Photo of two doctors in white coats outdoors" style="background:linear-gradient(180deg,#e9eef2 0%,#f4f5f4 60%,#8fb56a 100%)"></div>
  <h4>Supendie vitae lectus dict</h4>
  <p>Nullas tempus neque massa id mollis neque fesrli convallis ut. Morbi estr velit tincidunt quis felis etv consequat mollis nibhar. Aliquam porttitor</p>
  <span class="more">Read more ›</span>
  <div class="meta"><svg width="9" height="11" viewBox="0 0 18 22"><path d="M9 0a8 8 0 018 8c0 6-8 14-8 14S1 14 1 8a8 8 0 018-8z" fill="#7a7f8c"/></svg>12, Mill Road, Eastvale</div>
</article>

<!-- footer -->
<footer class="abs footer">
  <div class="abs logo" style="left:122px;top:60px"><span class="dot"></span>Eastvale Physiotherapy</div>
  <p class="about">Taking care of a sick child can be a frightening experience, we are extremely proud to have immediate assistance and advice.</p>

  <div class="hours">
    <h3>Working Hours</h3>
    <div class="row"><span>MON - FRI</span><span>7:00AM - 9:00PM</span></div>
    <div class="row"><span>SAT</span><span>8:00AM - 8:00PM</span></div>
    <div class="row"><span>SUN</span><span>Closed</span></div>
  </div>

  <div class="contact-box">
    <div class="emg">
      <svg width="26" height="26" viewBox="0 0 24 24"><path d="M6 2l4 5-2 3c1 3 3 5 6 6l3-2 5 4-3 4C10 21 3 14 2 5z" fill="#3f8f76"/></svg>
      <div><small>Emergency number</small><strong>300-555-0187</strong></div>
    </div>
    <div class="line"><svg width="14" height="11" viewBox="0 0 26 20"><rect x="1" y="1" width="24" height="18" fill="none" stroke="#fff" stroke-width="2.5"/><path d="M1 1l12 10L25 1" fill="none" stroke="#fff" stroke-width="2.5"/></svg>info@eastvaleclinic.example</div>
    <div class="line"><svg width="14" height="11" viewBox="0 0 26 20"><rect x="1" y="1" width="24" height="18" fill="none" stroke="#fff" stroke-width="2.5"/><path d="M1 1l12 10L25 1" fill="none" stroke="#fff" stroke-width="2.5"/></svg>care@eastvaleclinic.example</div>
    <div class="line"><svg width="14" height="13" viewBox="0 0 24 22"><path d="M12 1L1 11h3v10h6v-6h4v6h6V11h3z" fill="#fff"/></svg>48 Ferris Lane, Eastvale</div>
  </div>
</footer>
<div class="abs copyright">Copyright 2018 Eastvale Physiotherapy. All Rights Reserved.</div>

</body>
</html>
```